Full Desgin Webstore for selling products online
BrindleBazaar.net
Full Desgin Webstore for selling products online - Electronics
Creative Brief
Electronics
www.brindlebazaar.net
Selling online products company such as electronic devices, cosmetics, men's and women's clothes, computers and mobiles
Example design zorvani.com tupo.com
white
Dark red
left side
www.plomb.com
www.qirmaz.com
www.nelt.com.kw
i need too script example zorvani.com www.qirmaz.com www.plomb.com www.nelt.com.kw

```html
<!DOCTYPE html>
<html lang="en">
<head>
<meta charset="utf-8">
<title>BrindleBazaar.net – Online Store</title>
<link href="https://fonts.googleapis.com/css2?family=Fira+Sans:wght@400;500;600&family=Oswald:wght@400;500;600&display=swap" rel="stylesheet">
<style>
:root{
  --red:#c8232c;
  --red-dark:#a81b22;
  --ink:#333;
  --muted:#777;
  --line:#e2e2e2;
  --soft:#f2f2f2;
  --footer:#363636;
  --white:#fff;
}
*{box-sizing:border-box;margin:0;padding:0}
html,body{width:1200px;height:3005px;overflow:hidden}
body{position:relative;background:var(--white);font-family:"Fira Sans",sans-serif;color:var(--ink)}
.abs{position:absolute}

.topbar{left:0;top:0;width:1200px;height:33px;background:var(--soft);font-size:12px}
.topbar .contact{left:132px;top:9px;display:flex;gap:26px}
.topbar .contact span{display:flex;align-items:center;gap:5px}
.topbar .account{right:132px;top:9px;display:flex;gap:10px}
.caret{color:var(--red);font-size:9px}

.logo{left:132px;top:54px;font-weight:600;font-size:30px;color:var(--red);letter-spacing:-0.5px}
.logo small{font-size:12px;font-weight:400;margin-left:2px}
.search{left:562px;top:60px;width:357px;height:32px;border:1px solid #ccc;display:flex}
.search span{flex:1;font-style:italic;font-size:11px;color:#666;padding:9px 14px}
.search b{width:34px;background:#222;display:flex;align-items:center;justify-content:center}
.cart{left:942px;top:58px;display:flex;gap:10px;align-items:center}
.cart .ico{width:36px;height:32px;background:var(--red);display:flex;align-items:center;justify-content:center}
.cart .t{font-size:12px;line-height:14px}
.cart .t small{font-size:9px;color:#555}

.nav{left:0;top:119px;width:1200px;height:41px;background:var(--red)}
.nav .cat{position:absolute;left:132px;top:1px;width:153px;height:40px;background:var(--white);display:flex;align-items:center;gap:8px;padding-left:26px;font-size:15px}
.nav ul{position:absolute;left:285px;top:0;display:flex;list-style:none;height:41px}
.nav li{color:var(--white);font-size:15px;display:flex;align-items:center;justify-content:center;border-left:1px solid rgba(255,255,255,.25);height:41px}
.nav li:first-child{border-left:0}

.hero{left:0;top:160px;width:1200px;height:400px;background:linear-gradient(100deg,#8d96ad 0%,#c9b9a4 30%,#d8c9c2 55%,#bccadb 75%,#9fb0c6 100%)}
.hero-box{left:388px;top:306px;width:413px;height:112px;background:rgba(50,50,50,.72);text-align:center;color:var(--white)}
.hero-box .s{font-family:"Oswald",sans-serif;font-size:24px;margin-top:8px;letter-spacing:.5px}
.hero-box .b{font-family:"Oswald",sans-serif;font-weight:600;font-size:42px;line-height:46px;letter-spacing:.5px}
.dots{left:520px;top:533px;display:flex;gap:9px}
.dots i{width:12px;height:12px;border-radius:50%;background:var(--white);display:block}
.dots i.on{background:var(--red);border:2px solid var(--white)}

.promo{top:591px;width:288px;height:188px;background:#e5e1dc}
.promo .txt{position:absolute;left:14px;font-family:"Oswald",sans-serif}
.promo .red{color:var(--red);font-size:18px}
.promo .big{font-family:"Fira Sans",sans-serif;font-size:24px;color:#333;line-height:28px}
.promo .art{position:absolute;right:0;top:0;height:188px}

.panel{left:132px;width:936px;height:401px;border:1px solid var(--line);box-shadow:0 1px 3px rgba(0,0,0,.08)}
.tabs{position:absolute;left:12px;top:8px;width:910px;height:36px;border-bottom:1px solid var(--line)}
.tabs .arr{position:absolute;top:1px;width:27px;height:27px;border:1px solid #ccc;display:flex;align-items:center;justify-content:center;color:var(--red)}
.tabs .names{position:absolute;left:0;right:0;top:4px;display:flex;justify-content:center;font-size:17px}
.tabs .names span{padding:0 20px 10px}
.tabs .names span.on{color:var(--red);border-bottom:3px solid var(--red)}
.card{position:absolute;top:67px;width:168px;text-align:center}
.card .pic{width:168px;height:206px;background:linear-gradient(#f4f4f4,#e6e6e6)}
.card .pic.dark{background:#8a8a8a;position:relative}
.card .name{font-family:"Oswald",sans-serif;font-size:12px;margin-top:16px;letter-spacing:.2px}
.card .price{font-size:19px;margin-top:3px}
.card .stars{color:var(--red);font-size:13px;letter-spacing:3px;margin-top:1px}
.overlay{position:absolute;left:0;right:0;top:122px;display:flex;justify-content:center;gap:7px}
.overlay i{width:24px;height:24px;border-radius:50%;background:var(--white);display:flex;align-items:center;justify-content:center}
.buy{position:absolute;left:42px;top:160px;width:84px;height:22px;border-radius:11px;background:var(--red);color:var(--white);font-size:10px;font-weight:600;line-height:22px}

.sec-title{left:143px;width:912px;text-align:center;font-size:17px;color:var(--red);border-bottom:1px solid var(--line)}
.sec-title span{display:inline-block;padding:0 8px 8px;border-bottom:3px solid var(--red);margin-bottom:-1px}

.tile{display:flex;align-items:flex-end;justify-content:center;padding-bottom:10px;font-family:"Oswald",sans-serif;font-weight:500;font-size:19px;color:var(--white);letter-spacing:.6px;text-shadow:0 1px 3px rgba(0,0,0,.6)}

.brand{top:2163px;width:155px;height:85px;border:1px solid #ccc;display:flex;align-items:center;justify-content:center;font-size:24px;font-weight:600;color:#1d5fa8}
.circ-arr{top:2197px;width:20px;height:20px;border:1px solid #999;border-radius:50%;display:flex;align-items:center;justify-content:center;color:#888;font-size:11px}

.signup{left:0;top:2295px;width:1200px;height:198px;background:var(--soft);text-align:center}
.signup h2{font-family:"Oswald",sans-serif;font-weight:500;font-size:28px;color:var(--red);margin-top:46px;letter-spacing:.5px}
.signup p{font-size:11px;color:#555;margin-top:6px}
.signup .email{position:absolute;left:419px;top:119px;width:221px;height:34px;background:var(--white);border:1px solid #bbb;font-style:italic;font-size:11px;color:#777;text-align:left;padding:10px 14px}
.signup .btn{position:absolute;left:650px;top:119px;width:130px;height:34px;background:var(--red);color:var(--white);font-size:15px;font-weight:500;line-height:34px}

.feat{top:2535px;width:220px;text-align:center;font-size:18px;color:#555}
.feat svg{display:block;margin:0 auto 14px}

.footer{left:0;top:2704px;width:1200px;height:257px;background:var(--footer);color:var(--white)}
.fcol{position:absolute;top:44px}
.fcol h3{font-weight:500;font-size:20px;letter-spacing:.3px;margin-bottom:10px}
.fcol ul{list-style:none}
.fcol li{font-size:12px;height:28px;display:flex;align-items:center;gap:10px}
.fcol li::before{content:"›";font-size:15px;color:#ccc}
.vline{position:absolute;top:44px;width:1px;height:180px;background:#4c4c4c}
.socialbox{width:174px;height:69px;border:1px solid #777;text-align:center;padding-top:6px;margin-bottom:6px}
.socialbox .n{font-size:19px;font-weight:500}
.socialbox .row{display:flex;justify-content:center;gap:8px;margin-top:6px}
.socialbox .row i{width:22px;height:22px;border-radius:50%;background:var(--white);display:block}

.bottom{left:0;top:2961px;width:1200px;height:44px;background:var(--white)}
.bottom .copy{position:absolute;left:132px;top:16px;font-size:12px;color:#444}
.pay{position:absolute;top:10px;height:26px;width:40px;border-radius:3px;font-size:9px;font-weight:500;display:flex;align-items:center;justify-content:center;background:#e4e4ea;color:#444}
</style>
</head>
<body>

<div class="abs topbar">
  <div class="abs contact">
    <span><svg width="12" height="12" viewBox="0 0 24 24"><path fill="#c8232c" d="M6.6 10.8a15 15 0 0 0 6.6 6.6l2.2-2.2c.3-.3.7-.4 1-.2 1.1.4 2.3.6 3.6.6.6 0 1 .4 1 1V20c0 .6-.4 1-1 1A17 17 0 0 1 3 4c0-.6.4-1 1-1h3.5c.6 0 1 .4 1 1 0 1.3.2 2.5.6 3.6.1.3 0 .7-.2 1z"/></svg>123-456-7890</span>
    <span><svg width="13" height="11" viewBox="0 0 24 18"><rect width="24" height="18" rx="2" fill="#c8232c"/><path d="M2 2l10 8 10-8" stroke="#fff" stroke-width="2" fill="none"/></svg>info@brindlebazaar.net</span>
  </div>
  <div class="abs account"><span>My Account <span class="caret">▼</span></span><span>| USD <span class="caret">▼</span></span></div>
</div>

<div class="abs logo">BrindleBazaar<small>.net</small></div>
<div class="abs search"><span>what are you wishing for today?</span><b><svg width="16" height="16" viewBox="0 0 24 24"><circle cx="10" cy="10" r="7" stroke="#fff" stroke-width="3" fill="none"/><path d="M15 15l6 6" stroke="#fff" stroke-width="3"/></svg></b></div>
<div class="abs cart">
  <div class="ico"><svg width="20" height="18" viewBox="0 0 24 22"><path d="M1 2h4l3 12h12l3-9H7" stroke="#fff" stroke-width="2" fill="none"/><circle cx="10" cy="19" r="2" fill="#fff"/><circle cx="18" cy="19" r="2" fill="#fff"/></svg></div>
  <div class="t">Shopping Cart<br><small>0 Item &nbsp;- $0.00</small></div>
</div>

<nav class="abs nav">
  <div class="cat"><svg width="15" height="12" viewBox="0 0 15 12"><rect width="15" height="2" fill="#c8232c"/><rect y="5" width="15" height="2" fill="#c8232c"/><rect y="10" width="15" height="2" fill="#c8232c"/></svg>Categories</div>
  <ul>
    <li style="width:113px">Home</li>
    <li style="width:117px">New <span style="font-size:10px;margin-left:4px">⌄</span></li>
    <li style="width:133px">Features <span style="font-size:10px;margin-left:4px">⌄</span></li>
    <li style="width:103px">Blog</li>
    <li style="width:134px">About Us</li>
    <li style="width:140px">Contact Us <span style="font-size:10px;margin-left:4px">⌄</span></li>
  </ul>
</nav>

<div class="abs hero" role="img" aria-label="Cosmetics arrangement: lipsticks, foundation bottles, compacts and makeup brushes"></div>
<div class="abs hero-box">
  <div class="s">BrindleBazaar EXCLUSIVE</div>
  <div class="b">DONEC MAGNA DIAM</div>
</div>
<div class="abs dots"><i></i><i></i><i class="on"></i><i></i><i></i><i></i><i></i><i></i></div>

<div class="abs promo" style="left:132px">
  <div class="art" role="img" aria-label="Woman holding colourful shopping bags" style="width:140px;background:linear-gradient(120deg,#e9d9d3,#e85b9a 60%,#c8232c)"></div>
  <div class="txt" style="top:50px"><div class="red">BIG FASHION DAY!</div><div class="big">Save Upto<br><span style="margin-left:26px;font-size:30px">50%</span><br><span style="margin-left:44px;font-size:15px">Off</span></div></div>
</div>
<div class="abs promo" style="left:456px;background:#eceae7">
  <div class="art" role="img" aria-label="Laptop, tablet and phone bundle" style="width:150px;background:linear-gradient(135deg,#eceae7,#b9c3cf 55%,#6f8fb8)"></div>
  <div class="txt" style="top:50px"><div class="red">COMBO DAY!</div><div class="big">Save Upto<br>50% <span style="font-size:13px">Off</span></div></div>
</div>
<div class="abs promo" style="left:780px">
  <div class="art" role="img" aria-label="Smartphone shown front and back" style="width:130px;background:linear-gradient(135deg,#e5e1dc,#a9a9a9 60%,#6d6d6d)"></div>
  <div class="txt" style="top:50px;font-size:15px"><div class="red" style="font-size:16px">EXCLUSIVE ON</div><div style="color:var(--red);font-family:'Fira Sans',sans-serif;font-weight:600;font-size:15px">BrindleBazaar</div><div style="margin-top:6px;color:#333">DONEC MAGNA DIAM</div><div style="font-family:'Fira Sans',sans-serif;color:#333;margin-top:2px">Only At &nbsp;<span style="font-size:19px">$1234</span></div></div>
</div>

<section class="abs panel" style="top:812px">
  <div class="tabs">
    <div class="arr" style="left:0">‹</div>
    <div class="names"><span>NEW ARRIVAL</span><span class="on">FEATURED PRODUCTS</span><span>BEST SELLERS</span></div>
    <div class="arr" style="right:0">›</div>
  </div>
  <div class="card" style="left:13px"><div class="pic" role="img" aria-label="Tablet with app icons"></div><div class="name">LOREM IPSUM DOLOR SIT AMET</div><div class="price">$246.00</div><div class="stars">★★★★★</div></div>
  <div class="card" style="left:199px"><div class="pic" role="img" aria-label="Smartphone with colourful home screen"></div><div class="name">LOREM IPSUM DOLOR SIT AMET</div><div class="price">$246.00</div><div class="stars">★★★★★</div></div>
  <div class="card" style="left:385px"><div class="pic dark" role="img" aria-label="Smartphone, hovered">
      <div class="overlay"><i><svg width="12" height="11" viewBox="0 0 24 22"><path d="M1 2h4l3 12h12l3-9H7" stroke="#c8232c" stroke-width="3" fill="none"/></svg></i><i><svg width="12" height="11" viewBox="0 0 24 22"><path d="M12 21 2 11a5.5 5.5 0 0 1 10-6 5.5 5.5 0 0 1 10 6z" fill="#c8232c"/></svg></i><i><svg width="11" height="11" viewBox="0 0 24 24"><circle cx="10" cy="10" r="7" stroke="#c8232c" stroke-width="3" fill="none"/><path d="M15 15l6 6" stroke="#c8232c" stroke-width="3"/></svg></i></div>
      <div class="buy">BUY NOW</div></div><div class="name">LOREM IPSUM DOLOR SIT AMET</div><div class="price">$246.00</div><div class="stars">★★★★★</div></div>
  <div class="card" style="left:570px"><div class="pic" role="img" aria-label="Smartphone with colourful home screen"></div><div class="name">LOREM IPSUM DOLOR SIT AMET</div><div class="price">$246.00</div><div class="stars">★★★★★</div></div>
  <div class="card" style="left:756px"><div class="pic" role="img" aria-label="Silver smartphone"></div><div class="name">LOREM IPSUM DOLOR SIT AMET</div><div class="price">$246.00</div><div class="stars">★★★★★</div></div>
</section>

<section class="abs panel" style="top:1243px">
  <div class="tabs">
    <div class="arr" style="left:0">‹</div>
    <div class="names"><span>MOST VIEWED</span><span class="on">DEAL OF THE DAY</span><span>SPECIAL PRODUCTS</span></div>
    <div class="arr" style="right:0">›</div>
  </div>
  <div class="card" style="left:13px"><div class="pic" role="img" aria-label="Eyeshadow palette and makeup brushes"></div><div class="name">LOREM IPSUM DOLOR SIT AMET</div><div class="price">$246.00</div><div class="stars">★★★★★</div></div>
  <div class="card" style="left:199px"><div class="pic" role="img" aria-label="Stack of colourful folded shirts"></div><div class="name">LOREM IPSUM DOLOR SIT AMET</div><div class="price">$246.00</div><div class="stars">★★★★★</div></div>
  <div class="card" style="left:385px"><div class="pic dark" role="img" aria-label="Smartphone, hovered">
      <div class="overlay"><i><svg width="12" height="11" viewBox="0 0 24 22"><path d="M1 2h4l3 12h12l3-9H7" stroke="#c8232c" stroke-width="3" fill="none"/></svg></i><i><svg width="12" height="11" viewBox="0 0 24 22"><path d="M12 21 2 11a5.5 5.5 0 0 1 10-6 5.5 5.5 0 0 1 10 6z" fill="#c8232c"/></svg></i><i><svg width="11" height="11" viewBox="0 0 24 24"><circle cx="10" cy="10" r="7" stroke="#c8232c" stroke-width="3" fill="none"/><path d="M15 15l6 6" stroke="#c8232c" stroke-width="3"/></svg></i></div>
      <div class="buy">BUY NOW</div></div><div class="name">LOREM IPSUM DOLOR SIT AMET</div><div class="price">$246.00</div><div class="stars">★★★★★</div></div>
  <div class="card" style="left:570px"><div class="pic" role="img" aria-label="Compact powder, lipstick and mascara"></div><div class="name">LOREM IPSUM DOLOR SIT AMET</div><div class="price">$246.00</div><div class="stars">★★★★★</div></div>
  <div class="card" style="left:756px"><div class="pic" role="img" aria-label="Black DSLR camera"></div><div class="name">LOREM IPSUM DOLOR SIT AMET</div><div class="price">$246.00</div><div class="stars">★★★★★</div></div>
</section>

<div class="abs sec-title" style="top:1670px"><span>SHOP BY CATEGORY</span></div>
<div class="abs tile" style="left:143px;top:1727px;width:268px;height:161px;background:linear-gradient(135deg,#6b3f24,#3a2213)" role="img" aria-label="Vintage camera on a wooden table">ELECTRONIC DEVICES</div>
<div class="abs tile" style="left:143px;top:1909px;width:268px;height:161px;background:linear-gradient(90deg,#b9562a,#d94b4b 30%,#5a8de0 55%,#e0a040 80%,#c77b4a)" role="img" aria-label="Smartphones in a row of colours against a sunset">MOBILE &amp; TABLETS</div>
<div class="abs tile" style="left:430px;top:1727px;width:338px;height:343px;background:linear-gradient(180deg,#e8e8e6,#cfcfcc 60%,#6d6d6b)" role="img" aria-label="Flat lay of jacket, striped top, beanie, boots and jeans">CLOTHING &amp; ACCESSORIES</div>
<div class="abs tile" style="left:788px;top:1727px;width:267px;height:161px;background:linear-gradient(135deg,#d9dde3,#4a6fa5 55%,#2a3a55)" role="img" aria-label="Tablet and laptop on a desk">COMPUTERS &amp; ACCESSORIES</div>
<div class="abs tile" style="left:788px;top:1909px;width:267px;height:161px;background:linear-gradient(135deg,#c9865a,#a55a33 55%,#6b3a20)" role="img" aria-label="Red heels, sunglasses and cosmetics on wood">BEAUTY &amp; HEALTH</div>

<div class="abs sec-title" style="top:2107px"><span>OUR BRANDS</span></div>
<div class="abs circ-arr" style="left:72px">←</div>
<div class="abs brand" style="left:132px">Hexon</div>
<div class="abs brand" style="left:327px">Lunavo</div>
<div class="abs brand" style="left:521px">Dorrel</div>
<div class="abs brand" style="left:717px;color:#999">Pomely</div>
<div class="abs brand" style="left:912px">Samvira</div>
<div class="abs circ-arr" style="left:1099px">→</div>

<section class="abs signup">
  <h2>SIGN UP TO RECEIVE THE LATEST PRODUCT UPDATES</h2>
  <p>Lorem ipsum dolor sit amet, consectetur adipiscing elit. In metus mauris, blandit id porttitor porttitor, interdum eget arcu. Duis dui neque,</p>
  <div class="email">Your Email</div>
  <div class="btn">SUBSCRIBE</div>
</section>

<div class="abs feat" style="left:138px">
  <svg width="64" height="70" viewBox="0 0 64 70"><path d="M32 4 58 18 32 32 6 18z" fill="#c8232c"/><path d="M6 22 30 35v31L6 53z" fill="#444"/><path d="M58 22 34 35v31l24-13z" fill="#555"/><path d="M19 11 45 25M45 11 19 25" stroke="#fff" stroke-width="3"/></svg>
  100% Genuine Brands</div>
<div class="abs feat" style="left:373px">
  <svg width="64" height="70" viewBox="0 0 64 70"><rect x="4" y="4" width="40" height="58" rx="4" fill="none" stroke="#444" stroke-width="4"/><rect x="30" y="24" width="30" height="44" rx="4" fill="#fff" stroke="#c8232c" stroke-width="4"/><rect x="40" y="60" width="10" height="3" fill="#c8232c"/></svg>
  Secure Shopping</div>
<div class="abs feat" style="left:606px">
  <svg width="76" height="68" viewBox="0 0 76 68"><rect x="2" y="8" width="40" height="38" fill="#c8232c"/><text x="22" y="32" font-family="Oswald,sans-serif" font-size="14" fill="#fff" text-anchor="middle" font-weight="600">FREE</text><path d="M44 20h16l12 14v12H44z" fill="#444"/><rect x="2" y="46" width="70" height="6" fill="#444"/><circle cx="18" cy="56" r="8" fill="#fff" stroke="#444" stroke-width="4"/><circle cx="58" cy="56" r="8" fill="#fff" stroke="#444" stroke-width="4"/></svg>
  Free Shipping</div>
<div class="abs feat" style="left:842px">
  <svg width="66" height="70" viewBox="0 0 66 70"><path d="M33 8a27 27 0 1 1-26 20" fill="none" stroke="#444" stroke-width="5"/><path d="M10 24a27 27 0 0 1 20-16" fill="none" stroke="#c8232c" stroke-width="5" stroke-dasharray="4 4"/><text x="34" y="45" font-family="Fira Sans,sans-serif" font-size="24" font-weight="600" fill="#444" text-anchor="middle">24</text></svg>
  24/7 Support</div>

<footer class="abs footer">
  <div class="fcol" style="left:132px"><h3>QUICK LINKS</h3><ul><li>Home</li><li>New</li><li>Features</li><li>Blog</li><li>About Us</li><li>Contact Us</li></ul></div>
  <div class="vline" style="left:318px"></div>
  <div class="fcol" style="left:382px"><h3>OUR SERVICE</h3><ul><li>Delivery Method</li><li>Express Inquiry</li><li>Returns</li><li>Terms Of Service</li><li>Privacy Policy</li><li>Faq</li></ul></div>
  <div class="vline" style="left:574px"></div>
  <div class="fcol" style="left:638px"><h3>MY ACCOUNT</h3><ul><li>My Account</li><li>My Cart</li><li>Checkout</li><li>My Wishlist</li><li>Login</li><li>Sign Up</li></ul></div>
  <div class="vline" style="left:829px"></div>
  <div class="fcol" style="left:894px"><h3>STAY CONNECTED</h3>
    <div class="socialbox"><div class="n">BrindleBazaar</div><div class="row"><i></i><i></i><i></i><i></i></div></div>
    <ul><li>Sell On BrindleBazaar</li><li>Careers</li><li>Advertise Your Products</li></ul></div>
</footer>

<div class="abs bottom">
  <div class="copy">© 2016. BRINDLEBAZAAR.NET ALL RIGHTS RESERVED.</div>
  <div class="pay" style="left:837px">Quilla</div>
  <div class="pay" style="left:885px">Ferno</div>
  <div class="pay" style="left:933px">Brask</div>
  <div class="pay" style="left:981px">Olvin</div>
  <div class="pay" style="left:1029px">Tesmo</div>
</div>

</body>
</html>
```